Business Card and Word .doc header and footer required

I need a business card designed for my cybersecurity consulting company. Also required, is a header and footer to be ued for my word documents.
Attached is the Logo design, font and rgb used.

Industry/Entity Type

Cyber Security Consulting

Contact Information for Business Card

Name, Phone, email, website

Colors
0054AA
0677BA
7BADD7
CADEEF
E8F1F8

Requirements
Must have
• Sleek, modern

```html
<!DOCTYPE html>
<html lang="en">
<head>
<meta charset="utf-8">
<title>Harbor Ridge Consulting – Business Card</title>
<link href="https://fonts.googleapis.com/css2?family=Poppins:wght@400;500;600;700&display=swap" rel="stylesheet">
<style>
  :root {
    --navy: #141d3d;
    --navy-deep: #0e1530;
    --blue: #0677ba;
    --blue-strong: #0054aa;
    --blue-soft: #7badd7;
    --blue-pale: #cadeef;
    --blue-mist: #e8f1f8;
    --white: #ffffff;
    --stage: #2a2b2f;
  }
  * { box-sizing: border-box; margin: 0; padding: 0; }
  html, body { width: 1200px; height: 800px; overflow: hidden; }
  body {
    background: var(--stage);
    font-family: "Poppins", sans-serif;
    display: flex;
    align-items: center;
    justify-content: center;
    gap: 48px;
  }
  .card {
    width: 525px;
    height: 300px;
    border-radius: 24px;
    position: relative;
    overflow: hidden;
    box-shadow: 0 18px 40px rgba(0,0,0,.45);
  }
  .card-back {
    background: linear-gradient(135deg, #1c2a55 0%, var(--navy) 55%, var(--navy-deep) 100%);
  }
  .card-front { background: var(--white); }

  .brand-decor {
    position: absolute;
    right: -70px;
    top: 30px;
    width: 250px;
    height: 250px;
    border-radius: 50%;
    background: linear-gradient(135deg, var(--blue-mist) 0%, var(--blue-pale) 100%);
  }

  .holder {
    position: absolute;
    top: 26px;
    right: 30px;
    text-align: right;
    line-height: 1.15;
  }
  .holder-name {
    color: var(--blue);
    font-weight: 600;
    font-size: 17px;
    letter-spacing: .2px;
  }
  .holder-role {
    color: var(--navy);
    font-weight: 500;
    font-size: 13px;
  }

  .brand {
    position: absolute;
    left: 42px;
    top: 96px;
    display: flex;
    align-items: center;
    gap: 14px;
  }
  .brand-dot {
    width: 44px;
    height: 44px;
    border-radius: 50%;
    background: var(--blue);
    flex: none;
  }
  .brand-name {
    color: var(--navy);
    font-weight: 700;
    font-size: 27px;
    line-height: 1;
    letter-spacing: .3px;
  }
  .brand-sub {
    display: flex;
    align-items: center;
    gap: 8px;
    margin-top: 6px;
    color: var(--blue);
    font-weight: 500;
    font-size: 11px;
    letter-spacing: 5px;
  }
  .brand-sub::before, .brand-sub::after {
    content: "";
    height: 1.5px;
    width: 22px;
    background: var(--blue);
  }

  .contacts {
    position: absolute;
    left: 42px;
    bottom: 30px;
    list-style: none;
    display: flex;
    flex-direction: column;
    gap: 7px;
  }
  .contact {
    display: flex;
    align-items: center;
    gap: 10px;
    color: var(--navy);
    font-size: 13px;
    font-weight: 400;
  }
  .contact-icon {
    width: 18px;
    height: 18px;
    border-radius: 50%;
    border: 1.5px solid var(--blue);
    display: flex;
    align-items: center;
    justify-content: center;
  }
  .contact-icon svg { width: 10px; height: 10px; }
</style>
</head>
<body>
  <div class="card card-back" role="img" aria-label="Card back: navy field with a repeated brand-mark pattern in spot gloss and silver foil"></div>

  <div class="card card-front">
    <div class="brand-decor" role="img" aria-label="Large brand mark decoration"></div>

    <div class="holder">
      <p class="holder-name">DANIEL MARSH</p>
      <p class="holder-role">DIRECTOR</p>
    </div>

    <div class="brand">
      <span class="brand-dot"></span>
      <div>
        <p class="brand-name">HARBOR RIDGE</p>
        <p class="brand-sub">CONSULTING</p>
      </div>
    </div>

    <ul class="contacts">
      <li class="contact">
        <span class="contact-icon">
          <svg viewBox="0 0 10 10"><path d="M2 1.5 L3.6 1.5 L4.2 3.3 L3.2 4 Q4 6 6 6.8 L6.7 5.8 L8.5 6.4 L8.5 8 Q4 8.5 1.5 2 Z" fill="var(--blue)"/></svg>
        </span>
        040 1234 5678
      </li>
      <li class="contact">
        <span class="contact-icon">
          <svg viewBox="0 0 10 10"><rect x="1" y="2.5" width="8" height="5.5" rx=".6" fill="none" stroke="var(--blue)" stroke-width="1"/><path d="M1.3 3 L5 5.8 L8.7 3" fill="none" stroke="var(--blue)" stroke-width="1"/></svg>
        </span>
        daniel@harborridge.com.au
      </li>
      <li class="contact">
        <span class="contact-icon">
          <svg viewBox="0 0 10 10"><circle cx="5" cy="5" r="3.8" fill="none" stroke="var(--blue)" stroke-width="1"/><ellipse cx="5" cy="5" rx="1.6" ry="3.8" fill="none" stroke="var(--blue)" stroke-width=".8"/><path d="M1.2 5 H8.8" stroke="var(--blue)" stroke-width=".8"/></svg>
        </span>
        www.harborridge.com.au
      </li>
    </ul>
  </div>
</body>
</html>
```